Creative Brief
Buisness Card Larkfield Homes
Card for Larkfield
Professional
Cal Dorsey
Constrution Supervisor
Larkfield Homes
PO Box 530618
Houston, Texas 77064
cdorsey@larkfield-homes.example
www.larkfield-homes.example
Logo file

```html
<!DOCTYPE html>
<html lang="en">
<head>
<meta charset="utf-8">
<title>Larkfield Homes Stationery</title>
<link href="https://fonts.googleapis.com/css2?family=Lato:wght@400;700&display=swap" rel="stylesheet">
<style>
:root{
  --stage:#2a2a2a;
  --paper:#ffffff;
  --ink:#111111;
  --band:#0d0d0d;
  --gold:#d9a21b;
  --silver:#b9b9b9;
  --text-grey:#555555;
  --rule:#cfcfcf;
}
*{box-sizing:border-box;margin:0;padding:0}
html,body{width:1200px;height:422px;overflow:hidden}
body{background:var(--stage);font-family:'Lato',sans-serif;position:relative;color:var(--ink)}
.sheet{position:absolute;background:var(--paper);overflow:hidden;box-shadow:0 2px 6px rgba(0,0,0,.5)}
.brand{display:flex;align-items:center;gap:4px;color:var(--gold);font-weight:700;text-transform:uppercase;letter-spacing:.5px;line-height:1;white-space:nowrap}
.brand-mark{background:var(--gold);flex:none}
.top-band{position:absolute;left:0;top:0;width:100%;background:var(--band);border-bottom:2px solid var(--gold)}
.contact{position:absolute;color:#ddd;font-size:5px;line-height:7px;white-space:nowrap}
.contact span{display:block}
.swoosh{position:absolute;left:0;bottom:0;width:100%}

/* business cards */
.card-front{left:22px;top:112px;width:118px;height:56px;background:var(--band)}
.card-front .brand{position:absolute;left:7px;top:8px;font-size:5px}
.card-front .brand-mark{width:8px;height:8px}
.card-front .person{position:absolute;right:7px;top:8px;text-align:right;color:#eee;font-size:4px;line-height:6px}
.card-front .person b{color:var(--gold);font-size:5px}
.card-back{left:22px;top:176px;width:118px;height:56px;background:var(--band)}
.card-back .brand{position:absolute;left:8px;top:10px;font-size:6px}
.card-back .brand-mark{width:10px;height:10px}
.card-back .contact{left:8px;top:28px;font-size:4.5px;line-height:6px}

/* letterhead */
.letterhead{left:250px;top:8px;width:232px;height:406px}
.letterhead .top-band,.fax .top-band{height:36px}
.top-band .brand{position:absolute;left:12px;top:7px;font-size:5px;flex-direction:column;gap:3px}
.top-band .brand-mark{width:14px;height:13px}
.top-band .contact{left:140px;top:7px}
.faint-name{position:absolute;left:0;right:0;top:150px;display:flex;flex-direction:column;align-items:center;gap:8px;color:var(--gold);opacity:.18;font-weight:700;font-size:12px;text-transform:uppercase;letter-spacing:1px}
.faint-name i{display:block;width:52px;height:52px;background:var(--gold)}

/* fax */
.fax{left:500px;top:8px;width:258px;height:406px}
.fax-title{position:absolute;left:12px;top:46px;font-size:11px;font-weight:700}
.fax-table{position:absolute;left:12px;top:62px;width:234px;border-collapse:collapse;font-size:4.5px}
.fax-table td{border:1px solid var(--rule);height:8px;padding:0 3px;color:var(--text-grey)}
.fax-options{position:absolute;left:12px;top:116px;display:flex;gap:8px;font-size:4.5px;color:var(--text-grey);white-space:nowrap}
.fax-options span::before{content:"";display:inline-block;width:4px;height:4px;border:1px solid #888;margin-right:2px;vertical-align:-1px}
.fax-comments{position:absolute;left:12px;top:132px;font-size:4.5px;color:var(--text-grey)}
.fax-web{position:absolute;left:0;right:0;bottom:36px;text-align:center;font-size:4.5px;color:var(--text-grey)}

/* envelopes */
.envelope-back{left:823px;top:60px;width:353px;height:132px}
.envelope-front{left:823px;top:221px;width:353px;height:163px}
.flap{position:absolute;left:0;top:0;width:100%;height:100%}
.envelope-back .brand{position:absolute;left:166px;top:20px;font-size:4.5px;flex-direction:column;gap:2px}
.envelope-back .brand-mark{width:12px;height:10px}
.envelope-front .top-band{height:32px;border-bottom:2px solid var(--silver)}
.envelope-front .brand{position:absolute;left:10px;top:7px;font-size:4.5px;flex-direction:column;gap:2px}
.envelope-front .brand-mark{width:11px;height:9px}
.envelope-front .return{position:absolute;left:10px;top:40px;font-size:4.5px;line-height:6px;color:var(--text-grey)}
</style>
</head>
<body>

<svg width="0" height="0" style="position:absolute">
  <defs>
    <linearGradient id="gold-grad" x1="0" x2="1">
      <stop offset="0" stop-color="#f0c24a"/><stop offset="1" stop-color="#a8740c"/>
    </linearGradient>
    <linearGradient id="silver-grad" x1="0" x2="1">
      <stop offset="0" stop-color="#e6e6e6"/><stop offset="1" stop-color="#8a8a8a"/>
    </linearGradient>
  </defs>
</svg>

<section class="sheet card-front">
  <div class="brand"><i class="brand-mark"></i>Larkfield Homes</div>
  <div class="person"><b>Cal Dorsey</b><br>Construction Supervisor</div>
  <svg class="swoosh" viewBox="0 0 118 16" height="16" preserveAspectRatio="none"><path d="M0 16 L0 9 Q60 3 118 8 L118 16Z" fill="url(#gold-grad)"/><path d="M55 16 Q88 6 118 9 L118 16Z" fill="url(#silver-grad)"/></svg>
</section>

<section class="sheet card-back">
  <div class="brand"><i class="brand-mark"></i>Larkfield Homes</div>
  <div class="contact"><span>PO Box 530618, Houston, Texas 77064</span><span>cdorsey@larkfield-homes.example</span><span>www.larkfield-homes.example</span></div>
</section>

<section class="sheet letterhead">
  <header class="top-band">
    <div class="brand"><i class="brand-mark"></i>Larkfield Homes</div>
    <div class="contact"><span>PO Box 530618</span><span>Houston, Texas 77064</span><span>www.larkfield-homes.example</span></div>
  </header>
  <div class="faint-name"><i></i>Larkfield Homes</div>
  <svg class="swoosh" viewBox="0 0 232 30" height="30" preserveAspectRatio="none"><path d="M0 30 L0 14 Q110 8 232 18 L232 30Z" fill="url(#gold-grad)"/><path d="M110 30 Q175 12 232 15 L232 30Z" fill="url(#silver-grad)"/></svg>
</section>

<section class="sheet fax">
  <header class="top-band">
    <div class="brand"><i class="brand-mark"></i>Larkfield Homes</div>
    <div class="contact"><span>PO Box 530618</span><span>Houston, Texas 77064</span><span>www.larkfield-homes.example</span></div>
  </header>
  <h1 class="fax-title">FAX</h1>
  <table class="fax-table">
    <tr><td>To:</td><td>From:</td></tr>
    <tr><td>Fax:</td><td>Pages:</td></tr>
    <tr><td>Phone:</td><td>Date:</td></tr>
    <tr><td>Re:</td><td>CC:</td></tr>
  </table>
  <div class="fax-options"><span>Urgent</span><span>For Review</span><span>Please Comment</span><span>Please Reply</span><span>Please Recycle</span></div>
  <p class="fax-comments">Comments:</p>
  <p class="fax-web">www.larkfield-homes.example</p>
  <svg class="swoosh" viewBox="0 0 258 30" height="30" preserveAspectRatio="none"><path d="M0 30 L0 14 Q120 8 258 18 L258 30Z" fill="url(#gold-grad)"/><path d="M120 30 Q190 12 258 15 L258 30Z" fill="url(#silver-grad)"/></svg>
</section>

<section class="sheet envelope-back">
  <svg class="flap" viewBox="0 0 353 132" preserveAspectRatio="none">
    <path d="M0 0 H353 V26 L190 62 Q176 66 162 62 L0 26Z" fill="#0d0d0d"/>
    <path d="M0 26 L162 62 Q176 66 190 62 L353 26" fill="none" stroke="#d9a21b" stroke-width="2"/>
    <path d="M0 132 L150 82 M353 132 L202 82" stroke="#e2e2e2" stroke-width="1"/>
  </svg>
  <div class="brand"><i class="brand-mark"></i>Larkfield</div>
</section>

<section class="sheet envelope-front">
  <header class="top-band">
    <div class="brand"><i class="brand-mark"></i>Larkfield Homes</div>
  </header>
  <p class="return">Larkfield Homes<br>PO Box 530618<br>Houston, Texas 77064</p>
  <svg class="swoosh" viewBox="0 0 353 28" height="28" preserveAspectRatio="none"><path d="M0 28 L0 14 Q170 6 353 18 L353 28Z" fill="url(#gold-grad)"/><path d="M160 28 Q255 10 353 13 L353 28Z" fill="url(#silver-grad)"/></svg>
</section>

</body>
</html>
```